Microblading website contest - Make it colorful

Beauty salon focusing on microblading need a better website template. Please make a 1 page site mobile optimized and nicer layout with better color formulation. Would love interactive images in the site. You can use stock images and if approve we can pay for it.
Current site:
tessawynkelpeony.com

Inspiration:
https://framqueue.net/shots/41877260-Microblading-HomePage
https://framqueue.net/shots/7914026-Lunetto-Microblading-Eyebrow-Beauty-Salon-Pagewright-Theme

Target Market(s)

women

Industry/Entity Type

beauty salon

Number of Pages Required

1 page

Font styles to use
Serif
Decorative
Script

Requirements
Nice to have
• As pretty as possible

```html
<!DOCTYPE html>
<html lang="en">
<head>
<meta charset="utf-8">
<title>Peony Brow House Tessa — Microblading Studio</title>
<link href="https://fonts.googleapis.com/css2?family=Yellowtail&family=Rubik:wght@500;600;700&family=Arimo:wght@400;700&display=swap" rel="stylesheet">
<style>
:root{
  --blush:#fde4e4;
  --rose:#f2b1b5;
  --rose-deep:#eba2a8;
  --wine:#9c3b4e;
  --wine-light:#c57a86;
  --ink:#2a2a2c;
  --body:#5d5d62;
  --slate:#55575d;
  --white:#ffffff;
}
*{box-sizing:border-box;margin:0;padding:0}
html,body{width:1200px;height:4598px;overflow:hidden}
body{position:relative;background:var(--white);font-family:"Arimo",Arial,sans-serif;color:var(--body)}
.abs{position:absolute}
.script{font-family:"Yellowtail",cursive;color:var(--wine);font-weight:400;white-space:nowrap}
.heading{font-family:"Rubik",Arial,sans-serif;font-weight:700;color:var(--ink);white-space:nowrap}
.btn{position:absolute;display:flex;align-items:center;justify-content:center;gap:8px;
  background:linear-gradient(90deg,var(--wine),var(--wine-light));color:var(--white);
  font-family:"Rubik",sans-serif;font-weight:600;font-size:16px;border-radius:22px 0 22px 0;white-space:nowrap}
.rule{position:absolute;height:2px;background:var(--rose-deep)}
.photo{position:absolute}

/* hero */
.hero-band{left:0;top:0;width:1200px;height:679px;background:var(--blush)}
.logo{left:111px;top:54px;font-size:21px;line-height:30px}
.nav{left:384px;top:60px;display:flex;font-size:14px;color:#6a6a6e;white-space:nowrap}
.nav span{margin-right:32px}
.hero-lead{left:111px;top:176px;font-size:54px;line-height:64px}
.hero-title{left:108px;top:248px;font-size:50px;line-height:70px}
.hero-text{left:111px;top:402px;width:420px;font-size:16px;line-height:28px}
.scroll{left:111px;top:630px;font-size:11px;color:#444}

/* about */
.about-lead{left:622px;top:1010px;font-size:36px;line-height:44px}
.about-title{left:622px;top:1060px;font-size:40px;line-height:50px}
.about-text{left:622px;top:1124px;width:460px;font-size:14px;line-height:26px}
.video-frame{left:264px;top:1473px;width:597px;height:400px;background:var(--blush);border:2px solid var(--wine)}

/* services */
.services{left:0;top:1997px;width:1200px;height:989px;background:var(--slate)}
.center{width:1200px;text-align:center;left:0}
.svc-lead{top:2070px;font-size:38px;line-height:46px;color:#f0a8b0}
.svc-title{top:2118px;font-size:42px;line-height:54px;color:var(--white)}
.svc-intro{top:2218px;font-size:14px;line-height:31px;color:#f1f1f1}
.card-title{font-family:"Arimo",sans-serif;font-size:20px;color:var(--white);line-height:34px}
.card-list{list-style:none;font-size:14px;color:#f1f1f1;line-height:31px}
.card-list li{display:flex;align-items:flex-start;gap:10px}
.card-list li svg{flex:none;margin-top:10px}
.card-link{font-size:13px;font-weight:700;color:#f3a6ae;text-decoration:underline;line-height:27px}

/* care */
.care-lead{left:111px;top:3070px;font-size:36px;line-height:44px}
.care-title{left:111px;top:3124px;font-size:40px;line-height:50px}
.feature{left:563px;top:3272px;width:369px;height:437px;background:rgba(242,177,181,.93);border:2px solid var(--wine)}
.feature h3{position:absolute;left:44px;top:168px;font-family:"Arimo",sans-serif;font-weight:400;font-size:24px;color:var(--wine);white-space:nowrap}
.feature p{position:absolute;left:44px;top:218px;width:280px;font-size:13px;line-height:30px;color:#8a5c62}
.vbar{top:3272px;width:68px;height:437px;background:var(--rose);border:2px solid var(--wine);display:flex;align-items:center;justify-content:center}
.vbar span{transform:rotate(-90deg);white-space:nowrap;font-size:22px;color:var(--wine)}

/* join */
.join-lead{left:111px;top:3922px;font-size:36px;line-height:44px}
.join-title{left:111px;top:3976px;font-size:40px;line-height:50px}
.contact{left:111px;display:flex;align-items:center;gap:16px;font-size:15px;color:#444}
.contact i{display:block;width:30px;height:30px;border-radius:50%;flex:none}

/* footer */
.footer{left:0;top:4545px;width:1200px;height:53px;background:var(--rose-deep);font-size:11px;color:#7a2f3d}
</style>
</head>
<body>

<!-- HERO -->
<div class="abs hero-band"></div>
<div class="abs script logo">Peony Brow House Tessa</div>
<nav class="abs nav"><span>About Us</span><span>Services</span><span>Gallery</span><span>Shop</span><span>Academy</span><span>Customer Feedback</span></nav>
<div class="btn" style="left:943px;top:46px;width:145px;height:43px">Contact Us <span>»</span></div>

<div class="abs script hero-lead">Welcome To</div>
<h1 class="abs heading hero-title">Peony Brow House<br>Tessa</h1>
<p class="abs hero-text">I must explain to you how all this mistaken idea of denouncing pleasure and praising pain was born and I will give you a complete account</p>
<div class="btn" style="left:111px;top:509px;width:155px;height:43px">Get Started <span>»</span></div>
<div class="abs scroll"><span style="color:var(--wine);margin-right:10px">⌄</span>Scroll Down</div>

<div class="photo" role="img" aria-label="Decorative striped circle" style="left:559px;top:186px;width:160px;height:210px;border-radius:50%;background:rgba(235,162,168,.35)"></div>
<svg class="abs" style="left:559px;top:180px" width="560" height="560" viewBox="0 0 560 560"><path d="M2 560V250A270 250 0 0 1 552 250V560" fill="none" stroke="#eba2a8" stroke-width="2"/></svg>
<div class="photo" style="left:986px;top:736px;width:171px;height:171px;background:var(--rose-deep)"></div>
<div class="photo" role="img" aria-label="Close-up portrait of a woman shaping her eyebrow with tweezers" style="left:618px;top:186px;width:455px;height:637px;border-radius:228px 228px 0 0;background:linear-gradient(160deg,#c99c88,#8a6b5e 60%,#b0948a)"></div>

<!-- ABOUT -->
<div class="photo" role="img" aria-label="Portrait of the microblading artist in a white top" style="left:111px;top:993px;width:446px;height:625px;background:linear-gradient(180deg,#bdbdbd,#9a9a9a)"></div>
<div class="abs script about-lead">Who We Are</div>
<h2 class="abs heading about-title">About Tessa</h2>
<div class="rule" style="left:884px;top:1086px;width:81px"></div>
<div class="abs about-text">
<p>Tessa has 7 years of microblading experience. She graduated from VelaTouch United States. After, she studied in Linaria Academy, a global top brand from Germany. She was personally guided by the brand CEO Marek Dovan and the first China Master Lin Hao.</p>
<p style="margin-top:26px">After earning award of ArcBrows Artist in 2019. Tessa continued her practice microblading until she won the world's first ArcBrows Master in Taiwan in 2021. She is currently the only certificated Master technician in Taiwan. She also holds a shading and ArcBright Master.</p>
</div>
<div class="btn" style="left:622px;top:1379px;width:155px;height:39px;font-size:15px">Read More <span>»</span></div>

<div class="abs video-frame"></div>
<div class="photo" role="img" aria-label="Microblading treatment video still" style="left:300px;top:1509px;width:525px;height:329px;background:linear-gradient(100deg,#3a2a24,#7a5a4a 55%,#2a2220)"></div>
<svg class="abs" style="left:325px;top:1747px" width="64" height="64" viewBox="0 0 64 64"><circle cx="32" cy="32" r="31" fill="#b56a78" opacity=".55"/><circle cx="32" cy="32" r="22" fill="#a34a5c"/><path d="M27 23l13 9-13 9z" fill="#fff"/></svg>
<div class="abs" style="left:407px;top:1768px;font-family:Rubik,sans-serif;font-weight:600;font-size:16px;color:#fff">Play Video</div>

<!-- SERVICES -->
<div class="abs services"></div>
<div class="abs center script svc-lead">What We Do</div>
<h2 class="abs center heading svc-title">Specialized Service</h2>
<div class="rule" style="left:561px;top:2191px;width:78px;background:#fff"></div>
<p class="abs center svc-intro">We treat every client as our friends and family. We give you the most sincere advise and best quality and service.<br>We do not only follow the trend. We hear you, and want you to love it forever.</p>

<div class="photo" role="img" aria-label="Woman in a towel turban looking into a mirror" style="left:111px;top:2313px;width:314px;height:237px;border-radius:90px 0 0 0;background:linear-gradient(135deg,#e9e4e2,#c9b7ae)"></div>
<div class="photo" role="img" aria-label="Smiling woman with smoky eye makeup and red nails" style="left:443px;top:2313px;width:314px;height:237px;background:linear-gradient(135deg,#b9846a,#6e4634)"></div>
<div class="photo" role="img" aria-label="Artist performing eyebrow treatment on a client" style="left:775px;top:2313px;width:313px;height:237px;border-radius:0 0 90px 0;background:linear-gradient(135deg,#d8c6bf,#f1e6e2)"></div>

<svg width="0" height="0" style="position:absolute"><defs><symbol id="tick" viewBox="0 0 12 12"><rect x="1" y="1" width="10" height="10" rx="2" fill="none" stroke="#fff" stroke-width="1.4"/><path d="M3.5 6l2 2 3.5-4" fill="none" stroke="#fff" stroke-width="1.4"/></symbol></defs></svg>

<div class="abs" style="left:126px;top:2578px;width:300px">
<div class="card-title">NATURAL BROWS</div>
<ul class="card-list" style="margin-top:6px"><li><svg width="12" height="12"><use href="#tick"/></svg>Microblading</li><li><svg width="12" height="12"><use href="#tick"/></svg>Hand-drawing hair lines</li></ul>
<div class="card-link" style="margin-top:6px">For all skin type</div>
</div>
<div class="abs" style="left:458px;top:2578px;width:300px">
<div class="card-title">POWDER EYELINER<br>(NATURAL EYESHADOW)</div>
<ul class="card-list" style="margin-top:6px"><li><svg width="12" height="12"><use href="#tick"/></svg>Extend eyeline at end of the eye</li><li>With a touch of ligh eyeshadow vision</li></ul>
<div class="card-link" style="margin-top:6px">For those who like to have an eye<br>makeup filter</div>
<div class="card-link" style="margin-top:6px">24/7 | Eye-shape adjustment</div>
</div>
<div class="abs" style="left:790px;top:2578px;width:300px">
<div class="card-title">SCALP MICROPIGMENTATION</div>
<ul class="card-list" style="margin-top:6px"><li><svg width="12" height="12"><use href="#tick"/></svg>Add destiny to the thinning area</li><li><svg width="12" height="12"><use href="#tick"/></svg>Seamless and Undetectable</li><li><svg width="12" height="12"><use href="#tick"/></svg>Accommodates your skin tone &amp; natural hair color</li><li><svg width="12" height="12"><use href="#tick"/></svg>Providing the appearance of hair</li></ul>
<div class="card-link" style="margin-top:8px">For restoring hairline | Bald spots |<br>Scar covering</div>
</div>
<div class="btn" style="left:511px;top:2865px;width:178px;height:43px;background:#fff;color:var(--wine)">View Services <span>»</span></div>

<!-- CARE -->
<div class="abs script care-lead">Let us take care of it</div>
<h2 class="abs heading care-title">Your Eyebrows And Beauty</h2>
<div class="rule" style="left:682px;top:3152px;width:77px"></div>
<div class="btn" style="left:932px;top:3104px;width:156px;height:41px;font-size:15px">View More <span>»</span></div>

<div class="photo" role="img" aria-label="Smiling woman with voluminous curly hair" style="left:111px;top:3229px;width:528px;height:506px;background:linear-gradient(135deg,#c9a487,#8f6348)"></div>
<div class="abs feature">
<svg style="position:absolute;left:46px;top:76px" width="68" height="68" viewBox="0 0 68 68"><circle cx="34" cy="34" r="33" fill="#9c3b4e"/><circle cx="34" cy="31" r="9" fill="none" stroke="#fff" stroke-width="2"/><path d="M30 42h8M31 46h6" stroke="#fff" stroke-width="2"/></svg>
<h3>European Latest Technique</h3>
<p>We study European-style natural hair flow, improve and make it suitable for Asians</p>
<div class="btn" style="left:44px;top:320px;width:154px;height:43px">Get Started <span>»</span></div>
</div>
<div class="abs vbar" style="left:945px"><span>Licensed Microblading Artist</span></div>
<div class="abs vbar" style="left:1020px"><span>Years of experience</span></div>

<!-- JOIN -->
<div class="abs script join-lead">Join With Us</div>
<h2 class="abs heading join-title">More Services</h2>
<div class="rule" style="left:416px;top:4007px;width:78px"></div>
<div class="abs contact" style="top:4059px"><i style="background:#d8589a"></i>Ig : tessapeonybrowsarcbrowsmaster</div>
<div class="abs contact" style="top:4111px"><i style="background:#2c64c2"></i>Fb : tessapeonybrows</div>
<div class="abs contact" style="top:4163px"><i style="background:#d42a2a"></i>Video : @tessabrows</div>
<div class="abs contact" style="top:4214px"><i style="background:#3fb84a"></i>WeChat : tessabrows</div>
<div class="abs contact" style="top:4262px;align-items:flex-start;line-height:28px"><i style="background:linear-gradient(var(--wine-light),var(--wine))"></i><span>2750 Alder Row #118, Brookvale, NY 11490 , Peony Brow<br>House Inc</span></div>
<div class="btn" style="left:111px;top:4352px;width:155px;height:43px">Contact Us <span>»</span></div>

<div class="photo" role="img" aria-label="Decorative striped circle" style="left:955px;top:3852px;width:185px;height:185px;border-radius:50%;background:rgba(235,162,168,.4)"></div>
<div class="photo" role="img" aria-label="Smiling woman with long wavy hair and red nails" style="left:600px;top:3852px;width:488px;height:618px;border-radius:244px 244px 0 0;background:linear-gradient(150deg,#b88a66,#6b4631)"></div>

<!-- FOOTER -->
<footer class="abs footer">
<span class="abs" style="left:111px;top:20px">© Copyright 2023 | All Rights Reserved.</span>
<span class="abs" style="left:819px;top:20px">Privacy Policy</span>
<span class="abs" style="left:940px;top:20px">|</span>
<span class="abs" style="left:991px;top:20px">Terms Of Services</span>
</footer>

</body>
</html>
```